Utility Contractor looking for a new website

Water and wastewater utility contractor looking to create a new website that highlights our various services. We are looking for modern web presence that can be updated with current projects and new services as we grow. We have an existing logo that we would like to incorporate into the overall design of the site
Updates

Hi, Thank you for all the design submissions. I have had some time to review and have eliminated the ones I feel are not what I am looking for. Based on the designs that remain, I am looking for a clean (not to many bold colours), modern look that is not to busy (long scrolling page), Thanks, Dean

Target Market(s)

project managers, strata boards, owners, people who make decisions as to who operates their water/wastewater system

Industry/Entity Type

Utility

Font styles to use
Sans Serif

Requirements
Must have
• A min page that describes the company and what we do, A page for each of our services that outlines the service and the benefits of it. the look must be consistent throughout. additionally each service page should have some images related to the service

```html
<!DOCTYPE html>
<html lang="en">
<head>
<meta charset="utf-8">
<title>Clearline Utilities Ltd. — Water and Wastewater Utility Contractor</title>
<link rel="stylesheet" href="https://fonts.googleapis.com/css2?family=Roboto:wght@300;400;500;700&display=swap">
<style>
  :root {
    --brand-navy: #16365c;
    --brand-blue: #1b6fb8;
    --heading-blue: #1567b3;
    --text-dark: #2a2a2a;
    --header-top: #cfe6f3;
    --header-bottom: #eef6fb;
    --content-bg: #eef5f8;
    --footer-blue: #2f86c8;
    --footer-deep: #1f6fb3;
    --dot-active: #3bb38a;
    --white: #ffffff;
  }
  * { box-sizing: border-box; margin: 0; padding: 0; }
  html, body {
    width: 1200px; height: 1165px; overflow: hidden;
    font-family: "Roboto", Arial, sans-serif;
    background: var(--content-bg);
    color: var(--text-dark);
  }
  .page { position: relative; width: 1200px; height: 1165px; }

  /* Header */
  .site-header {
    position: absolute; left: 0; top: 0; width: 1200px; height: 110px;
    background: linear-gradient(180deg, var(--header-top), var(--header-bottom));
    box-shadow: 0 2px 4px rgba(40, 90, 130, 0.18);
    z-index: 2;
  }
  .brand {
    position: absolute; left: 183px; top: 34px;
    display: flex; align-items: center; gap: 10px;
    color: var(--brand-navy); font-weight: 700; font-size: 24px;
    line-height: 25px; letter-spacing: 0.3px; text-transform: uppercase;
  }
  .brand-mark { width: 14px; height: 14px; border-radius: 50%; background: var(--brand-navy); }
  .main-nav {
    position: absolute; top: 45px; left: 633px;
    display: flex; align-items: center;
  }
  .main-nav a {
    display: block; height: 34px; line-height: 34px; padding: 0 15px;
    color: #3a3a3a; text-decoration: none; font-size: 14.5px; text-transform: uppercase;
    border-radius: 3px;
  }
  .main-nav a.is-current {
    color: var(--white); padding: 0 16px;
    background: linear-gradient(180deg, #6cb3ef, #3d8fdb);
  }

  /* Hero */
  .hero {
    position: absolute; left: 0; top: 110px; width: 1200px; height: 469px;
    background:
      radial-gradient(ellipse 560px 90px at 640px 210px, rgba(70, 150, 205, 0.45), rgba(70, 150, 205, 0) 100%),
      radial-gradient(ellipse 380px 200px at 200px 200px, rgba(110, 175, 215, 0.35), rgba(110, 175, 215, 0) 100%),
      linear-gradient(180deg, #eaf5fb 0%, #d6ebf6 55%, #b4d8ee 100%);
  }
  .hero-title {
    position: absolute; right: 174px; top: 324px;
    color: var(--heading-blue); font-weight: 400; font-size: 31px; text-transform: uppercase;
    text-align: right; line-height: 36px;
  }
  .hero-subtitle {
    position: absolute; right: 174px; top: 369px;
    color: var(--heading-blue); font-weight: 400; font-size: 19.5px; text-transform: uppercase;
    text-align: right;
  }
  .slider-dots { position: absolute; left: 936px; top: 408px; display: flex; gap: 8px; }
  .slider-dots span { width: 12px; height: 12px; border-radius: 50%; background: var(--white); }
  .slider-dots span.is-active { background: var(--dot-active); }

  /* Intro blocks */
  .intro-block { position: absolute; top: 626px; }
  .intro-block h2 {
    color: var(--heading-blue); font-weight: 400; font-size: 19.5px; text-transform: uppercase;
    margin-bottom: 4px;
  }
  .intro-block p { font-size: 12.5px; line-height: 22.3px; text-align: justify; color: var(--text-dark); }
  .read-more {
    display: block; text-align: right; color: var(--brand-blue);
    font-size: 12.5px; text-decoration: none; margin-top: -4px;
  }
  .welcome { left: 177px; width: 344px; }
  .welcome .read-more { margin-right: 4px; }
  .services { left: 716px; width: 314px; top: 627px; }
  .services-photo {
    position: absolute; left: 552px; top: 629px; width: 153px; height: 119px;
    border-radius: 3px;
    background: linear-gradient(180deg, #b7d3e8 0%, #c8cfcf 35%, #8a7a66 70%, #a9a9a2 100%);
  }

  /* Experience */
  .experience-photo {
    position: absolute; left: 190px; top: 795px; width: 188px; height: 188px; border-radius: 50%;
    background: radial-gradient(circle at 45% 45%, #f4efe6, #d9d2c4 70%, #cfc8ba);
  }
  .experience { position: absolute; left: 417px; top: 812px; width: 600px; }
  .experience h2 {
    color: var(--heading-blue); font-weight: 400; font-size: 31px; line-height: 38px; letter-spacing: 0.2px;
  }
  .experience p { margin-top: 8px; margin-left: 2px; font-size: 14px; line-height: 24px; }

  /* Footer */
  .site-footer {
    position: absolute; left: 0; top: 1021px; width: 1200px; height: 144px;
    background:
      radial-gradient(ellipse 260px 120px at 180px 110px, rgba(20, 90, 160, 0.35), rgba(20, 90, 160, 0)),
      radial-gradient(ellipse 300px 140px at 1080px 60px, rgba(90, 160, 215, 0.4), rgba(90, 160, 215, 0)),
      linear-gradient(180deg, var(--footer-blue), var(--footer-deep));
    color: var(--white);
  }
  .footer-nav { position: absolute; left: 177px; top: 44px; display: flex; font-size: 14px; text-transform: uppercase; }
  .footer-nav a { color: var(--white); text-decoration: none; }
  .footer-nav .sep { margin: 0 7px; }
  .copyright { position: absolute; left: 177px; top: 74px; font-size: 11px; }
  .social-title { position: absolute; left: 681px; top: 44px; font-size: 14px; text-transform: uppercase; }
  .social-note { position: absolute; left: 681px; top: 74px; font-size: 11px; }
  .social-links { position: absolute; left: 861px; top: 47px; display: flex; gap: 9px; }
  .social-links a { width: 36px; height: 36px; border-radius: 50%; background: var(--white); display: block; }
</style>
</head>
<body>
<div class="page">
  <header class="site-header">
    <div class="brand"><span class="brand-mark"></span><span>Clearline<br>Utilities Ltd.</span></div>
    <nav class="main-nav">
      <a href="#" class="is-current">Home</a>
      <a href="#">About</a>
      <a href="#">Products</a>
      <a href="#">Blog</a>
      <a href="#">Contacts</a>
    </nav>
  </header>

  <section class="hero" role="img" aria-label="Illustration of a flowing blue water wave with splashes and bubbles">
    <h1 class="hero-title">Water and Wastewater</h1>
    <p class="hero-subtitle">Utility Contractor</p>
    <div class="slider-dots"><span></span><span class="is-active"></span><span></span><span></span><span></span></div>
  </section>

  <article class="intro-block welcome">
    <h2>Welcome!</h2>
    <p>Lorem Ipsum is simply dummy text of the printing and typesetting industry. Lorem Ipsum has been the industry's standard dummy text ever since the 1500s, when an unknown printer took a galley of type and scrambled</p>
    <a class="read-more" href="#">Read more &gt;&gt;</a>
  </article>

  <div class="services-photo" role="img" aria-label="Photo of a wastewater treatment plant with circular clarifier tanks"></div>
  <article class="intro-block services">
    <h2>Our Services</h2>
    <p>Lorem Ipsum is simply dummy text of the printing and typesetting industry. Lorem Ipsum has been the industry's standard dummy text ever since the 1500s, when an unknown printer took a galley of type and scrambled</p>
    <a class="read-more" href="#">Read more &gt;&gt;</a>
  </article>

  <div class="experience-photo" role="img" aria-label="Round photo of a woman drinking a glass of clean water"></div>
  <section class="experience">
    <h2>With over 10 years of<br>experience in the water filter market.</h2>
    <p>Lorem Ipsum is simply dummy text of the printing and typesetting industry. Lorem Ipsum has been the industry's standard dummy text ever sinc</p>
  </section>

  <footer class="site-footer">
    <nav class="footer-nav">
      <a href="#">Home</a><span class="sep">|</span>
      <a href="#">About</a><span class="sep">|</span>
      <a href="#">Products</a><span class="sep">|</span>
      <a href="#">Blog</a><span class="sep">|</span>
      <a href="#">Contacts</a>
    </nav>
    <p class="copyright">© 2014 Privacy Policy</p>
    <p class="social-title">Social Networks</p>
    <p class="social-note">Bayarsety kertya aset aplicaboes</p>
    <div class="social-links">
      <a href="#" aria-label="Social network 1"></a>
      <a href="#" aria-label="Social network 2"></a>
      <a href="#" aria-label="News feed"></a>
      <a href="#" aria-label="Social network 3"></a>
    </div>
  </footer>
</div>
</body>
</html>
```